Small but growing painting company. Have built up a steady client base. Want to start having a more professional look. Want to start with changing my business cards, and also getting new logo and tee shirts.

Target Market(s)

Home owners, property management companies, all ages 30-70

Industry/Entity Type

Painting And Decorating

Contact Information for Business Card

Bright Ridge Painting LLC Mark Delvecchi 630-584-3907 interior, exterior, vaulted ceiling, drywall repair, pressure washing, kitchen cabinets, epoxy, garage floors,

Font styles to use
Sans Serif
Other font styles liked:
• Harrington

Colors
0355a3
ffffff
ec1f27
000000
3176b5
0493ce
474747
b7b7b7

Requirements
Must have
• Creative, something that doesn’t look like every other painting card.
Nice to have
• I would like something with an arrow or something going to a point

```html
<!DOCTYPE html>
<html lang="en">
<head>
<meta charset="utf-8">
<title>Bright Ridge Painting LLC – Business Card</title>
<link rel="stylesheet" href="https://fonts.googleapis.com/css2?family=Montserrat:wght@400;500;600;700;800&display=swap">
<style>
  :root {
    --brand-blue: #0a4ea3;
    --paper: #ffffff;
    --backdrop: #e4e5e8;
    --shadow: rgba(0, 0, 0, 0.18);
  }
  * { margin: 0; padding: 0; box-sizing: border-box; }
  html, body {
    width: 1200px;
    height: 857px;
    overflow: hidden;
    background: var(--backdrop);
    font-family: "Montserrat", Arial, sans-serif;
  }
  .stage {
    position: relative;
    width: 1200px;
    height: 857px;
  }
  .card {
    position: absolute;
    top: 280px;
    width: 520px;
    height: 297px;
    overflow: hidden;
    box-shadow: 0 6px 18px var(--shadow);
  }
  .card--front { left: 50px; background: var(--paper); }
  .card--back { left: 630px; background: var(--brand-blue); }

  /* Wordmark */
  .wordmark {
    font-weight: 700;
    line-height: 1.05;
    letter-spacing: 0.02em;
  }
  .card--front .wordmark {
    position: absolute;
    left: 34px;
    top: 92px;
    font-size: 15px;
    color: var(--brand-blue);
  }
  .card--back .wordmark {
    position: absolute;
    left: 0;
    right: 0;
    top: 108px;
    text-align: center;
    font-size: 28px;
    color: var(--paper);
  }

  /* Name block */
  .owner {
    position: absolute;
    right: 40px;
    top: 36px;
    text-align: right;
    color: var(--brand-blue);
  }
  .owner__name {
    font-weight: 800;
    font-size: 19px;
    letter-spacing: 0.1em;
    text-transform: uppercase;
  }
  .owner__role {
    font-weight: 400;
    font-size: 13px;
    margin-top: 3px;
    letter-spacing: 0.03em;
  }

  /* Phone band */
  .phone-band {
    position: absolute;
    left: 262px;
    right: 0;
    top: 98px;
    height: 46px;
    background: var(--brand-blue);
    border-radius: 23px 0 0 23px;
    display: flex;
    align-items: center;
    padding-left: 22px;
    gap: 14px;
    color: var(--paper);
  }
  .phone-band__number {
    font-weight: 600;
    font-size: 19px;
    letter-spacing: 0.1em;
  }

  /* Services */
  .services {
    position: absolute;
    left: 38px;
    top: 150px;
    list-style: none;
    color: var(--brand-blue);
    font-size: 10.5px;
    font-weight: 500;
    letter-spacing: 0.1em;
    text-transform: uppercase;
    line-height: 1.62;
  }
  .services li::before {
    content: "";
    display: inline-block;
    width: 4px;
    height: 4px;
    border-radius: 50%;
    background: var(--brand-blue);
    margin-right: 7px;
    vertical-align: middle;
  }
  .services__more { font-weight: 700; }

  /* Bottom tab */
  .name-tab {
    position: absolute;
    bottom: -14px;
    left: 216px;
    width: 200px;
    height: 44px;
    border-radius: 16px;
    display: flex;
    align-items: flex-start;
    justify-content: center;
    padding-top: 9px;
    font-weight: 700;
    font-size: 11.5px;
    letter-spacing: 0.01em;
  }
  .card--front .name-tab { background: var(--brand-blue); color: var(--paper); }
  .card--back .name-tab { background: var(--paper); color: var(--brand-blue); left: 230px; }
</style>
</head>
<body>
<main class="stage">
  <section class="card card--front" aria-label="Business card front">
    <div class="wordmark">Bright Ridge<br>Painting LLC</div>

    <div class="owner">
      <div class="owner__name">Mark Delvecchi</div>
      <div class="owner__role">Founder / CEO</div>
    </div>

    <div class="phone-band">
      <svg class="phone-band__icon" width="20" height="20" viewBox="0 0 24 24" aria-hidden="true">
        <circle cx="12" cy="12" r="10.5" fill="none" stroke="#ffffff" stroke-width="1.8"/>
        <path d="M9.2 7.3l1.2 2.3c.2.4.1.8-.2 1.1l-.7.6c.6 1.3 1.6 2.3 2.9 2.9l.6-.7c.3-.3.7-.4 1.1-.2l2.3 1.2c.4.2.5.6.4 1l-.4 1.2c-.2.5-.7.8-1.2.7-3.8-.6-6.8-3.6-7.4-7.4-.1-.5.2-1 .7-1.2l1.2-.4c.4-.1.8 0 1 .4z" fill="#ffffff"/>
      </svg>
      <span class="phone-band__number">630-584-3907</span>
    </div>

    <ul class="services">
      <li>Interior I Exterior</li>
      <li>Vaulted Ceiling</li>
      <li>Drywall Repair</li>
      <li>Pressure Washing</li>
      <li class="services__more">And More...</li>
    </ul>

    <div class="name-tab">Bright Ridge Painting LLC</div>
  </section>

  <section class="card card--back" aria-label="Business card back">
    <div class="wordmark">Bright Ridge<br>Painting LLC</div>
    <div class="name-tab">Bright Ridge Painting LLC</div>
  </section>
</main>
</body>
</html>
```